Modernise Business Card

Our company has been operating for 10 years. With the start of the new decade we are looking to refresh our business card design. We manufacture a range of industrial product shipping to customers internationally. A copy of our current card, both sides, is attached. We are looking for a mature professional appearance.

```html
<!DOCTYPE html>
<html lang="en">
<head>
<meta charset="utf-8">
<title>Corvane business cards</title>
<link rel="stylesheet" href="https://fonts.googleapis.com/css2?family=Work+Sans:wght@400;500;700;800&display=swap">
<style>
  :root {
    --bg: #e7e8ea;
    --ink: #1f1f21;
    --card-dark: #222224;
    --card-light: #ffffff;
    --blue: #1a9be0;
    --text: #2a2a2c;
    --muted: #3a3a3c;
  }
  * { box-sizing: border-box; margin: 0; padding: 0; }
  html, body { width: 1200px; height: 912px; overflow: hidden; }
  body {
    background: var(--bg);
    font-family: "Work Sans", Arial, sans-serif;
    position: relative;
  }
  .card {
    position: absolute;
    width: 520px;
    height: 300px;
    border-radius: 14px;
    overflow: hidden;
    box-shadow: 0 10px 26px rgba(0,0,0,.18);
  }
  .card--front { left: 70px; top: 140px; background: var(--card-dark); }
  .card--back  { left: 610px; top: 472px; background: var(--card-light); }

  .wordmark {
    font-weight: 800;
    color: var(--blue);
    letter-spacing: -1px;
    display: flex;
    align-items: center;
    gap: 10px;
  }
  .wordmark__dot { width: 14px; height: 14px; background: var(--blue); display: inline-block; }

  .card--front .wordmark {
    position: absolute; left: 0; right: 0; top: 92px;
    justify-content: center; font-size: 66px;
  }
  .services {
    position: absolute; left: 0; right: 0; bottom: 34px;
    text-align: center; color: #fff;
    font-size: 11.5px; font-weight: 500; letter-spacing: 1.4px;
  }
  .services .sep { color: var(--blue); margin: 0 6px; }

  .card--back .wordmark {
    position: absolute; left: 34px; top: 34px; font-size: 44px;
  }
  .rule {
    position: absolute; left: 38px; right: 26px; top: 146px;
    height: 1px; background: var(--blue);
  }
  .person {
    position: absolute; right: 28px; top: 108px;
    color: var(--blue); font-size: 27px; font-weight: 500;
  }
  .address {
    position: absolute; right: 28px; top: 160px;
    text-align: right; font-size: 11.5px; line-height: 1.45;
    color: var(--muted); letter-spacing: .4px;
  }
  .contacts {
    position: absolute; left: 40px; top: 166px;
    list-style: none; font-size: 13.5px; line-height: 1.45;
    color: var(--text); letter-spacing: .5px;
  }
  .contacts li { display: flex; align-items: center; gap: 8px; }
  .contacts svg { width: 10px; height: 10px; flex: none; }
  .contacts .web-accent { color: var(--blue); }
  .band { position: absolute; left: 0; bottom: 0; width: 520px; height: 60px; }
</style>
</head>
<body>
  <section class="card card--front" aria-label="Card front">
    <div class="wordmark"><span class="wordmark__dot"></span>Corvane</div>
    <p class="services">HYDRAULIC ADAPTERS<span class="sep">|</span>HOSE FITTINGS<span class="sep">|</span>QUICK COUPLINGS</p>
  </section>

  <section class="card card--back" aria-label="Card back">
    <div class="wordmark"><span class="wordmark__dot"></span>Corvane</div>
    <h1 class="person">Lena Hartwell</h1>
    <div class="rule"></div>
    <p class="address">808-3,Lian Tai Building<br>117 Qingshan Road,<br>Haishu District<br>Ningbo 315000 China</p>
    <ul class="contacts">
      <li><svg viewBox="0 0 10 10"><path d="M2 1l2 2-1 1.2c.6 1.2 1.6 2.2 2.8 2.8L7 6l2 2-1.2 1.4C4.5 9.2.8 5.5.6 2.2z" fill="#1a9be0"/></svg>+86 150 2734 9618</li>
      <li><svg viewBox="0 0 10 10"><rect x="2.5" y=".8" width="5" height="8.4" rx="1" fill="none" stroke="#1a9be0" stroke-width="1.1"/></svg>+61 412 785 309</li>
      <li><svg viewBox="0 0 10 10"><rect x=".8" y="2" width="8.4" height="6" fill="none" stroke="#1a9be0" stroke-width="1.1"/><path d="M1 2.4l4 3 4-3" fill="none" stroke="#1a9be0" stroke-width="1.1"/></svg>lhartwell@corvanefittings.com</li>
      <li><svg viewBox="0 0 10 10"><circle cx="5" cy="5" r="4.2" fill="none" stroke="#1a9be0" stroke-width="1"/><path d="M.8 5h8.4M5 .8c-2 2.5-2 5.9 0 8.4M5 .8c2 2.5 2 5.9 0 8.4" fill="none" stroke="#1a9be0" stroke-width=".8"/></svg>www.<span class="web-accent">corvanefittings</span>.com</li>
    </ul>
    <svg class="band" viewBox="0 0 520 60" aria-hidden="true">
      <polygon points="0,52 392,16 382,60 0,60" fill="var(--blue)"/>
      <polygon points="402,15 520,4 520,60 392,60" fill="var(--ink)"/>
    </svg>
  </section>
</body>
</html>
```